Tideward Fuel Product design

We need a bottle design for our product. Tideward Fuel is a Gaming Nootropic made to increase Energy, Focus, Reaction time, and Clarity of an eSport gamer. It will be 40 servings a bottle. Currently, all the ingredients haven't been finalized so after the competition is over we will have to work with the designer to also make an ingredients label for the back of it. For the flavor, we will call it ember dusk.

The attachments included:. The velvet mongoose picture as a font style I like for the logo.
The K BOLT SURGEWAVE PICTURE IS WHAT WE WANT OUR DESIGN to look like something similar a clean and simple design that stands out!

K Bolt bottle is what our biggest competitors product looks like. The tideward fuel picture as the current logo we are using but can be changed.

Overall the pictures are just some references for what I could possibly want the design to look like however, I'm open to your designer's ideas and concepts you think would make for a cool looking Gaming Nootropic product bottle design. I appreciate everyone working on this and look forward to seeing your designs have a great day!

Target Market(s)

Gamers between the ages of 18-30

Industry/Entity Type

Health And Wellness

Requirements
Must have
• Tideward Fuel logo, state that it is for energy, focus, reaction, and clarity. state 40 serivngs. state flavor.

```html
<!DOCTYPE html>
<html lang="en">
<head>
<meta charset="utf-8">
<title>Tideward Fuel – Ember Dusk Label</title>
<link rel="stylesheet" href="https://fonts.googleapis.com/css2?family=Russo+One&family=Saira:ital,wght@0,600;1,700;1,800&family=Rajdhani:wght@600&family=Roboto:wght@400;700&display=swap">
<style>
  :root {
    --brand-blue: #2c52a6;
    --brand-blue-deep: #24489a;
    --sky: #b5d7f3;
    --sky-soft: #d9ebf9;
    --paper: #ffffff;
    --logo-grey: #8f969f;
    --rule-grey: #a9aeb4;
  }
  html, body {
    margin: 0;
    padding: 0;
    overflow: hidden;
    background: var(--paper);
  }
  .label {
    position: relative;
    width: 1200px;
    height: 985px;
    overflow: hidden;
    background: var(--paper);
  }
  .top-texture {
    position: absolute;
    left: 0; top: 0;
    width: 1200px; height: 134px;
    background: linear-gradient(180deg, var(--sky) 0%, var(--sky-soft) 100%);
  }
  .servings-tab {
    position: absolute;
    left: 985px; top: 0;
    width: 145px; height: 436px;
    background: var(--brand-blue);
    border-radius: 0 0 42px 42px;
    color: var(--paper);
    text-align: center;
    font-family: "Roboto", sans-serif;
    font-weight: 700;
  }
  .servings-count {
    position: absolute;
    left: 0; right: 0; top: 290px;
    font-size: 80px;
    line-height: 1;
  }
  .servings-word {
    position: absolute;
    left: 0; right: 0; top: 382px;
    font-size: 27px;
    line-height: 1;
  }
  .wordmark {
    position: absolute;
    left: 150px; top: 196px;
    width: 700px;
    text-align: center;
    font-family: "Russo One", sans-serif;
    color: var(--logo-grey);
    font-size: 120px;
    line-height: 148px;
    letter-spacing: 2px;
    margin: 0;
    font-weight: 400;
  }
  .wordmark span {
    display: block;
    transform: scaleY(1.25);
  }
  .wordmark-rule {
    position: absolute;
    left: 184px; top: 512px;
    width: 624px; height: 6px;
    background: var(--rule-grey);
  }
  .audience {
    position: absolute;
    left: 172px; top: 532px;
    margin: 0;
    font-family: "Saira", sans-serif;
    font-style: italic;
    font-weight: 700;
    font-size: 48px;
    line-height: 60px;
    letter-spacing: 6.5px;
    color: var(--brand-blue);
    white-space: nowrap;
  }
  .info-band {
    position: absolute;
    left: 0; top: 646px;
    width: 1200px; height: 339px;
  }
  .zero-stats {
    position: absolute;
    left: 0; top: 646px;
    width: 460px; height: 85px;
    font-family: "Saira", sans-serif;
    font-style: italic;
    color: var(--paper);
  }
  .zero-stat {
    position: absolute;
    top: 0;
    width: 120px;
    text-align: center;
  }
  .zero-value {
    display: block;
    font-weight: 800;
    font-size: 64px;
    line-height: 64px;
  }
  .zero-name {
    display: block;
    font-weight: 700;
    font-size: 15px;
    line-height: 18px;
    letter-spacing: 0.5px;
  }
  .flavor {
    position: absolute;
    left: 628px; top: 652px;
    margin: 0;
    font-family: "Saira", sans-serif;
    font-style: italic;
    font-weight: 800;
    font-size: 60px;
    line-height: 72px;
    letter-spacing: 5px;
    color: var(--paper);
    white-space: nowrap;
  }
  .benefits {
    position: absolute;
    left: 70px; top: 774px;
    width: 1030px;
    margin: 0;
    font-family: "Rajdhani", sans-serif;
    font-weight: 600;
    font-size: 58px;
    line-height: 70px;
    letter-spacing: 4px;
    color: var(--paper);
    text-align: center;
    white-space: nowrap;
  }
  .legal {
    position: absolute;
    left: 0; top: 850px;
    width: 1200px;
    margin: 0;
    font-family: "Roboto", sans-serif;
    font-size: 28px;
    line-height: 34px;
    letter-spacing: 1px;
    color: var(--paper);
    text-align: center;
    white-space: nowrap;
  }
</style>
</head>
<body>
<main class="label">
  <div class="top-texture" role="img" aria-label="Light blue slanted dash texture band"></div>

  <div class="servings-tab">
    <div class="servings-count">40</div>
    <div class="servings-word">servings</div>
  </div>

  <h1 class="wordmark"><span>TIDEWARD</span><span>FUEL</span></h1>
  <div class="wordmark-rule"></div>
  <p class="audience">FOR E-SPORT GAMERS</p>

  <svg class="info-band" width="1200" height="339" viewBox="0 0 1200 339" aria-hidden="true">
    <rect x="0" y="0" width="1200" height="339" fill="var(--brand-blue)"/>
    <polygon points="197,0 212,0 196,82 181,82" fill="var(--paper)"/>
    <polygon points="333,0 348,0 332,82 317,82" fill="var(--paper)"/>
    <polygon points="462,0 604,0 588,82 446,82" fill="var(--paper)"/>
  </svg>

  <div class="zero-stats">
    <div class="zero-stat" style="left:88px"><span class="zero-value">0</span><span class="zero-name">SUGAR</span></div>
    <div class="zero-stat" style="left:210px"><span class="zero-value">0</span><span class="zero-name">CALORIES</span></div>
    <div class="zero-stat" style="left:330px"><span class="zero-value">0</span><span class="zero-name">CAFFEINE</span></div>
  </div>

  <p class="flavor">EMBER DUSK</p>

  <p class="benefits">ENERGY | FOCUS | REACTION | CLARITY</p>
  <p class="legal">Dietary Supplement | Net Weight 12 OZ (118g)</p>
</main>
</body>
</html>
```